Website Redesign

Our current website (http://www.bramfordguard.com/) uses a standard word press template we basically want to keep. But there a few areas we want to improve the design of sub sites or single elements:

- Many graphics are just created from PowerPoint. Example: http://www.bramfordguard.com/product/server-plug-ins/ We want to improve the designs so they match the website overall design

- In many areas we use a lot of text and tabs (e.g. http://www.bramfordguard.com/product/#tab-id-1). I would like those to be merged into some graphics that contain some titles or short descriptions that can be expanded or linked to subpages.

- many of the template product bullet points look very much "out of the box" standard WP design. (e.g. http://www.bramfordguard.com/why-bramford/ or the feature list under http://www.bramfordguard.com/product/) Maybe we can also replace them with graphics where the graphic or the symbols already give the viewer an idea of the advantages/features.

- some pages need complete re-design (e.g. http://www.bramfordguard.com/resources/shop/ where the pic and the whole layout is not so professional)

- Symbols (like product boxes) also need a redesign http://www.bramfordguard.com/product-category/product/

Of course we are open to any other suggestion that improves the design but as well the whole navigation workflow which is currently very complex.

So we are looking for a designer who can do ALL the changes. BUT: as a start we would ask you to just pick ONE OR TWO elements from the list above and create a proposal for a re-design. If we like it we can continue from there on a hourly base....

2 page

• This is a word press website. If you can show that you can create some "interactive/linked" graphics --> would be great

```html
<!DOCTYPE html>
<html lang="en">
<head>
<meta charset="utf-8">
<title>Product Layers</title>
<link rel="stylesheet" href="https://fonts.googleapis.com/css2?family=Ubuntu:wght@500;700&display=swap">
<style>
  :root {
    --bg-light: #d7dac5;
    --bg-mid: #bcc6bc;
    --bg-dark: #a1a9b6;
    --stack-navy: #2e3a72;
    --stack-blue: #2b4f7c;
    --band-dark: #2b3868;
    --band-teal: #2a7a8c;
    --band-green: #2f9868;
    --people-top: #8c2b68;
    --people-bottom: #5a0f45;
    --tech-top: #c8c39c;
    --tech-bottom: #2e6c80;
    --rule: #1c2748;
    --label: #f4f2f2;
  }
  * { margin: 0; padding: 0; box-sizing: border-box; }
  html, body { width: 1200px; height: 800px; overflow: hidden; }
  body {
    position: relative;
    background: linear-gradient(120deg, var(--bg-light) 0%, var(--bg-mid) 50%, var(--bg-dark) 100%);
    font-family: "Ubuntu", sans-serif;
  }
  .product-stack {
    position: absolute;
    left: 440px; top: 262px;
    width: 320px; height: 282px;
    border-radius: 16px;
    overflow: hidden;
    background: linear-gradient(180deg, var(--stack-navy) 0%, var(--stack-blue) 40%);
    box-shadow: 0 4px 6px rgba(30, 30, 20, 0.45);
    display: flex;
    flex-direction: column;
  }
  .label {
    color: var(--label);
    font-weight: 700;
    font-size: 15px;
    letter-spacing: 1.55px;
    text-align: center;
    text-shadow: 0 1px 2px rgba(0, 0, 0, 0.55);
    line-height: 17px;
    white-space: nowrap;
  }
  .pillars {
    margin: 11px 13px 0 11px;
    height: 75px;
    display: flex;
    border-radius: 8px;
    overflow: hidden;
    border: 1px solid rgba(255, 255, 255, 0.25);
    box-shadow: 0 1px 3px rgba(0, 0, 0, 0.3);
  }
  .pillar {
    display: flex;
    align-items: center;
    justify-content: center;
  }
  .pillar--people {
    width: 148px;
    background: linear-gradient(180deg, var(--people-top), var(--people-bottom));
    padding-bottom: 2px;
  }
  .pillar--tech {
    flex: 1;
    background: linear-gradient(180deg, var(--tech-top), var(--tech-bottom));
    padding-bottom: 2px;
  }
  .layer {
    display: flex;
    align-items: center;
    justify-content: center;
    padding-left: 6px;
    border-top: 1px solid var(--rule);
  }
  .layer--scenarios { height: 41px; border-top: none; background: linear-gradient(90deg, #2f3b74, #2a5a80); }
  .layer--templates { height: 37px; background: linear-gradient(90deg, var(--band-dark), #2d4574); }
  .layer--training { height: 56px; background: linear-gradient(90deg, #2a5f86, var(--band-teal)); padding-bottom: 4px; }
  .layer--plugins { flex: 1; background: linear-gradient(100deg, #276a86 0%, var(--band-teal) 50%, var(--band-green) 100%); padding-bottom: 4px; }
</style>
</head>
<body>
  <section class="product-stack" aria-label="Product components">
    <div class="pillars">
      <div class="pillar pillar--people label">People Testing<br>and Education</div>
      <div class="pillar pillar--tech label">Technology<br>Assessments</div>
    </div>
    <div class="layer layer--scenarios label">Attack Scenarios</div>
    <div class="layer layer--templates label">Best Practice Attack Templates</div>
    <div class="layer layer--training label">Awareness Training &amp; Customizing</div>
    <div class="layer layer--plugins label">Convenience Plugins &amp; Tools</div>
  </section>
</body>
</html>
```